Zorvan Voltline Services requires a modern & sharp looking sign.

We need a sign to be designed for a local soccer club ground where advertising will take place. Text needs to be limited with only the basic information such as the logo/company name, website and mobile number. The EC40923 number must be placed somewhere in the sign.

The design should be similar to the flyer design attached, but in a more plain looking version.

Signage dimensions are 2050mm Wide x 900mm High.

Industry/Entity Type

Electrician

Requirements
Must have
• Logo/Company Name
• EC Number
• Website (www.zorvanvoltline.com.au)
• Phone Number
• - SAME COLOR SCHEME AS THE LOGO
• - SAME LIGHTNING BOLT TO THE RIGHT OF THE SIGN (REFER TO FLYER)
Should not have
• NO PICTURES

```html
<!DOCTYPE html>
<html lang="en">
<head>
<meta charset="utf-8">
<title>Zorvan Voltline Services – Ground Sign</title>
<link rel="stylesheet" href="https://fonts.googleapis.com/css2?family=Michroma&family=Open+Sans:wght@400&display=swap">
<style>
  :root {
    --backdrop: #1e1e1e;
    --sign-white: #ffffff;
    --sign-shade: #ececee;
    --brand-blue: #3a52a6;
    --steel-grey: #8a8c90;
    --licence-grey: #6b6b6b;
  }
  html, body {
    margin: 0;
    padding: 0;
    width: 1200px;
    height: 1000px;
    overflow: hidden;
    background: var(--backdrop);
  }
  .canvas {
    position: relative;
    width: 1200px;
    height: 1000px;
  }
  .ground-sign {
    position: absolute;
    left: 137px;
    top: 253px;
    width: 968px;
    height: 425px;
    display: block;
  }
  .sign-text {
    font-family: "Michroma", "Arial", sans-serif;
    fill: var(--brand-blue);
  }
  .licence-number {
    font-family: "Open Sans", "Arial", sans-serif;
    fill: var(--licence-grey);
  }
</style>
</head>
<body>
<main class="canvas">
  <svg class="ground-sign" viewBox="0 0 968 425" xmlns="http://www.w3.org/2000/svg" aria-label="Zorvan Voltline Services sign">
    <defs>
      <radialGradient id="sign-surface" cx="50%" cy="40%" r="70%">
        <stop offset="0%" stop-color="var(--sign-white)"/>
        <stop offset="100%" stop-color="var(--sign-shade)"/>
      </radialGradient>
    </defs>

    <rect class="sign-board" x="0" y="0" width="968" height="425" fill="url(#sign-surface)"/>

    <text class="licence-number" x="953" y="31" font-size="16" text-anchor="end">EC40923</text>

    <circle class="brand-circle" cx="125" cy="204" r="88" fill="none" stroke="var(--steel-grey)" stroke-width="16"/>

    <text class="sign-text brand-name" x="258" y="238" font-size="104" textLength="688" lengthAdjust="spacingAndGlyphs">ZORVAN</text>
    <text class="sign-text brand-name-sub" x="262" y="292" font-size="40" textLength="674" lengthAdjust="spacingAndGlyphs">VOLTLINE SERVICES</text>

    <text class="sign-text contact-phone" x="11" y="398" font-size="27" textLength="350" lengthAdjust="spacingAndGlyphs">TEL 0400 555 218</text>
    <text class="sign-text contact-web" x="955" y="398" font-size="25" text-anchor="end" textLength="555" lengthAdjust="spacingAndGlyphs">WWW.ZORVANVOLTLINE.COM.AU</text>
  </svg>
</main>
</body>
</html>
```